Business card needed for the Rydo of Dry Cleaning!

We need a slick business card design for a new company based out of Montreal called Casiers Plimo&Zet inc. (in French) and Plimo&Zet Lockers inc. (in English). We're the Rydo of Laundry. We offer services of dry cleaning, laundry (wash&fold), minor clothing alterations, shoe repair and parcel delivery through 24/7 secured and connected lockers. Ordres are placed through our mobile application. Real time notification are sent to customers when their order is ready for pickup. The lockers will be placed throughout the downtown area, in condo and office towers, where a high density of busy people converge. It is simple, user-friendly, and most importantly convenient. We're the out of the box dry cleaner, literally.

Target Market(s)

1) Professional workers wearing suits daily
2) Campus students living in residences
3) People using laundromats
4) Families with children/yuppies who prefer to use their time doing something else than laundry

Industry/Entity Type

Dry Cleaning

Contact Information for Business Card

Name / Annick-Solène Trudel
Title / CEO & Founder
Company Name / Casiers Plimo&Zet inc. | Plimo&Zet Lockers inc.
Website www.plimozet.ca

Requirements
Must have
• Text Logo: Plimo&Zet - Nettoyeurs 24/7 Cleaners
• Logo on one side and contact info on the other (bilingual)
• Minimalist, pure design
• "We care" for your belongings feeling
• Professional, technological, clean & fresh look
Should not have
• No busy visuals. No rainbow colors.

```html
<!DOCTYPE html>
<html lang="en">
<head>
<meta charset="utf-8">
<title>Plimo&amp;Zet Lockers – Business Card</title>
<link rel="stylesheet" href="https://fonts.googleapis.com/css2?family=Open+Sans:wght@400;600&display=swap">
<style>
  :root {
    --backdrop: #e6e8ec;
    --navy: #1f2f55;
    --cream: #eeeadb;
    --lilac-edge: #b9b8d2;
    --cyan: #1a9bd7;
    --ink-light: #e9edf3;
    --name-dark: #1f2f55;
    --name-light: #d7dde6;
  }
  * { margin: 0; padding: 0; box-sizing: border-box; }
  html, body { width: 1200px; height: 786px; overflow: hidden; }
  body {
    background: var(--backdrop);
    font-family: "Open Sans", Arial, sans-serif;
    position: relative;
  }
  .card {
    position: absolute;
    top: 250px;
    width: 500px;
    height: 286px;
    border-radius: 18px;
    background: var(--navy);
    overflow: hidden;
    box-shadow: 0 10px 26px rgba(20, 30, 60, 0.25);
  }
  .card--front { left: 70px; }
  .card--back { left: 630px; }

  .front__panel { position: absolute; inset: 0; }

  .company-name {
    position: absolute;
    font-weight: 600;
    white-space: nowrap;
  }
  .front .company-name {
    left: 36px; top: 112px;
    font-size: 30px;
    color: var(--name-dark);
  }

  .person {
    position: absolute;
    right: 30px;
    top: 44px;
    text-align: right;
  }
  .person__name {
    color: var(--cyan);
    font-weight: 600;
    font-size: 16px;
    letter-spacing: 0.5px;
    line-height: 1.25;
    text-transform: uppercase;
  }
  .person__title {
    color: var(--ink-light);
    font-size: 13px;
    margin-top: 4px;
  }

  .contact {
    position: absolute;
    right: 30px;
    bottom: 32px;
    list-style: none;
  }
  .contact__item {
    display: flex;
    justify-content: flex-end;
    align-items: center;
    gap: 8px;
    color: var(--ink-light);
    font-size: 13px;
    line-height: 22px;
  }
  .contact__icon {
    width: 16px; height: 16px;
    border-radius: 3px;
    background: var(--cyan);
    display: flex; align-items: center; justify-content: center;
  }

  .back .company-name {
    left: 0; right: 0; top: 108px;
    text-align: center;
    font-size: 34px;
    color: var(--name-light);
  }
  .back__url {
    position: absolute;
    left: 0; right: 0;
    top: 182px;
    text-align: center;
    color: var(--ink-light);
    font-size: 14px;
    letter-spacing: 0.6px;
  }
</style>
</head>
<body>

  <section class="card card--front front" aria-label="Business card, contact side">
    <svg class="front__panel" viewBox="0 0 500 286" aria-hidden="true">
      <path d="M0 0 H200 A130 150 0 0 1 200 286 H0 Z" fill="var(--lilac-edge)"/>
      <path d="M0 0 H196 A124 138 0 0 1 196 270 H0 Z" fill="var(--cream)"/>
    </svg>
    <p class="company-name">Plimo&amp;Zet</p>

    <div class="person">
      <p class="person__name">Annick-Solène<br>Trudel</p>
      <p class="person__title">CEO &amp; Founder</p>
    </div>

    <ul class="contact">
      <li class="contact__item">514-555-0142
        <span class="contact__icon">
          <svg width="10" height="10" viewBox="0 0 10 10"><path d="M2 1 L4 1 L4.6 3 L3.6 3.8 C4.2 5 5 5.8 6.2 6.4 L7 5.4 L9 6 L9 8 C5 8.5 1.5 5 2 1 Z" fill="#fff"/></svg>
        </span>
      </li>
      <li class="contact__item">info@plimozet.ca
        <span class="contact__icon">
          <svg width="10" height="8" viewBox="0 0 10 8"><rect x="0.5" y="0.5" width="9" height="7" fill="none" stroke="#fff"/><path d="M0.5 0.5 L5 4.5 L9.5 0.5" fill="none" stroke="#fff"/></svg>
        </span>
      </li>
      <li class="contact__item">www.plimozet.ca
        <span class="contact__icon">
          <svg width="10" height="10" viewBox="0 0 10 10"><circle cx="5" cy="5" r="4" fill="none" stroke="#fff"/><path d="M1 5 H9 M5 1 V9" stroke="#fff"/></svg>
        </span>
      </li>
    </ul>
  </section>

  <section class="card card--back back" aria-label="Business card, name side">
    <p class="company-name">Plimo&amp;Zet</p>
    <p class="back__url">www.plimozet.ca</p>
  </section>

</body>
</html>
```